Marketing Flyer for Plumber Referals

8.5" x11" Layout should be landscape not portrait. Create a bold, eye-catching flyer that highlights earning potential from referrals for water damage restoration. Use high-contrast colors like blue, yellow, and white, with bold fonts and dynamic layouts. Include images of restoration work, cash, and happy clients. Emphasize key benefits like $500 minimum payouts, fast payments, and unlimited income potential. Keep instructions simple: refer a client, we handle the work, you get paid. Add a clear call-to-action and display contact details prominently. Focus on professionalism and energy.

Target Market(s)

Plumbers and Contractor 8.5" x11" Layout should be landscape not portrait.

Industry/Entity Type

General Contractor

Colors
0054AA
0677BA
7BADD7
CADEEF
E8F1F8
EB3D1F
EC4F4E
F09395
F8D3D4
FCEDEE

Requirements
Must have
• 8.5" x11" Layout should be landscape not portrait.
Nice to have

```html
<!DOCTYPE html>
<html lang="en">
<head>
<meta charset="utf-8">
<title>Referral Flyer – Front and Back</title>
<link rel="stylesheet" href="https://fonts.googleapis.com/css2?family=Oswald:wght@500;700&family=Montserrat:wght@500;600;700;800&display=swap">
<style>
  :root{
    --page:#ece8e1;
    --paper:#eef0f2;
    --paper-dark:#dfe3e7;
    --orange:#f7941d;
    --orange-deep:#f15a24;
    --navy:#1d3a57;
    --ink:#1b1b24;
    --plum:#5b2c48;
    --red:#e3262c;
    --text:#2a2a33;
    --photo-wall:#c9c4be;
    --photo-warm:#a88a72;
    --photo-cash:#9fb5a2;
    --photo-people:#8fa9c4;
  }
  *{box-sizing:border-box;margin:0;padding:0}
  html,body{width:1200px;height:900px;overflow:hidden}
  body{background:var(--page);font-family:"Montserrat",sans-serif;color:var(--text);position:relative}

  .flyer{position:absolute;top:230px;width:570px;height:440px;overflow:hidden;
    background:radial-gradient(ellipse at 40% 40%,#f7f8f9 0%,var(--paper) 55%,var(--paper-dark) 100%);
    box-shadow:0 8px 22px rgba(0,0,0,.18)}
  .flyer--front{left:20px}
  .flyer--back{left:610px}

  /* ---------- front ---------- */
  .headline{position:absolute;left:26px;top:26px;font-family:"Oswald",sans-serif;text-transform:uppercase}
  .headline__kicker{font-size:15px;letter-spacing:7px;font-weight:500;
    background:linear-gradient(90deg,var(--orange-deep),var(--navy));-webkit-background-clip:text;background-clip:text;color:transparent}
  .headline__cash{font-size:96px;line-height:.9;font-weight:700;
    background:linear-gradient(180deg,var(--orange) 0%,var(--orange-deep) 100%);-webkit-background-clip:text;background-clip:text;color:transparent}
  .headline__amp{position:absolute;left:196px;top:44px;font-size:46px;font-weight:700;color:var(--orange-deep)}
  .headline__get{position:absolute;left:232px;top:20px;font-size:26px;font-weight:700;color:var(--orange-deep)}
  .headline__paid{position:absolute;left:232px;top:44px;font-size:52px;line-height:1;font-weight:700;color:var(--orange)}
  .headline__sub{position:absolute;left:232px;top:100px;width:200px;font-size:16px;font-weight:700;color:var(--navy);white-space:nowrap}

  .brand{position:absolute;right:26px;top:34px;display:flex;align-items:center;gap:8px}
  .brand__mark{width:14px;height:14px;background:var(--navy)}
  .brand__name{font-family:"Montserrat",sans-serif;font-weight:600;font-size:14px;color:var(--navy);letter-spacing:1px;text-transform:uppercase}
  .brand__tag{position:absolute;right:26px;top:54px;font-size:7px;letter-spacing:2px;color:var(--navy);font-weight:600;text-transform:uppercase}

  .front-photo{position:absolute;right:0;top:120px;width:290px;height:230px;
    background:linear-gradient(160deg,#f3f4f5 0%,var(--photo-wall) 70%,#b7b2ac 100%)}

  .band{position:absolute;left:0;color:#fff;font-weight:700;display:flex;align-items:center;padding-left:28px}
  .band--offer{top:160px;width:430px;height:30px;font-size:15px;background:var(--navy);
    clip-path:polygon(0 0,100% 0,94% 100%,0 100%)}
  .band--partner{top:194px;width:470px;height:28px;font-size:12px;
    background:linear-gradient(90deg,var(--plum),#3d2a48);clip-path:polygon(0 0,100% 0,95% 100%,0 100%)}

  .benefits{position:absolute;left:28px;top:240px;width:320px}
  .benefits__title{font-size:20px;font-weight:800;color:var(--ink);margin-bottom:10px}
  .benefits__list{list-style:none}
  .benefits__item{position:relative;padding-left:18px;font-size:10.5px;font-weight:600;line-height:1.9;color:var(--ink);white-space:nowrap}
  .benefits__item::before{content:"";position:absolute;left:2px;top:7px;width:7px;height:7px;background:var(--ink);transform:rotate(45deg)}
  .benefits__label{color:var(--orange)}

  .front-cta{position:absolute;left:28px;bottom:26px;font-size:22px;font-weight:800;color:var(--red)}

  /* ---------- back ---------- */
  .collage{position:absolute;right:0;top:0;width:330px;height:230px}
  .collage__tile{position:absolute;clip-path:polygon(25% 0,75% 0,100% 50%,75% 100%,25% 100%,0 50%)}
  .collage__tile--a{left:0;top:-20px;width:170px;height:160px;background:linear-gradient(150deg,#e9e3dc,var(--photo-warm))}
  .collage__tile--b{left:150px;top:-10px;width:150px;height:140px;background:linear-gradient(150deg,#b59a82,#6d5443)}
  .collage__tile--c{left:150px;top:105px;width:150px;height:135px;background:linear-gradient(150deg,#cfc9c0,#8c7766)}
  .cash{position:absolute;left:235px;top:125px;width:150px;height:95px;border-radius:6px;
    background:linear-gradient(135deg,#c7d4c5,var(--photo-cash))}
  .people{position:absolute;right:0;top:220px;width:136px;height:160px;
    background:linear-gradient(180deg,rgba(143,169,196,0) 0%,var(--photo-people) 40%,#6f8cac 100%);
    border-radius:68px 68px 0 0}

  .title{position:absolute;left:28px;top:40px;font-family:"Oswald",sans-serif;font-weight:700;text-transform:uppercase;line-height:.88}
  .title__small{font-size:22px;color:var(--orange)}
  .title__refer{font-size:78px;color:var(--orange);display:flex;align-items:flex-start;gap:6px}
  .title__a{font-size:20px;color:var(--navy);margin-top:6px}
  .title__flood{font-size:78px;color:var(--navy)}

  .steps-band{position:absolute;left:0;top:208px;width:300px;height:34px;background:var(--navy);color:#fff;
    font-size:19px;font-weight:800;display:flex;align-items:center;padding-left:28px;
    clip-path:polygon(0 0,100% 0,92% 100%,0 100%)}
  .steps{position:absolute;left:28px;top:252px;list-style:none;width:400px}
  .steps__item{font-size:10px;font-weight:700;color:var(--ink);line-height:1.35;margin-bottom:4px}
  .steps__detail{display:block;font-weight:500;padding-left:12px;font-size:9.5px;white-space:nowrap}

  .contact{position:absolute;left:28px;bottom:18px}
  .contact__pill{display:inline-block;background:var(--orange);color:#fff;font-size:10px;font-weight:700;border-radius:12px;padding:4px 12px}
  .contact__phone{font-size:24px;font-weight:800;color:var(--navy);line-height:1.15}
  .contact__web{font-size:12px;font-weight:700;color:var(--navy)}
</style>
</head>
<body>

<section class="flyer flyer--front" aria-label="Flyer front">
  <div class="front-photo" role="img" aria-label="Photo of a restoration worker on a ladder painting a bright wall"></div>

  <div class="headline">
    <div class="headline__kicker">Earn Unlimited</div>
    <div class="headline__cash">Cash</div>
    <span class="headline__amp">&amp;</span>
    <span class="headline__get">Get</span>
    <span class="headline__paid">Paid</span>
    <span class="headline__sub">To Refer a Flood</span>
  </div>

  <div class="brand"><span class="brand__mark"></span><span class="brand__name">Coastline Builders</span></div>
  <div class="brand__tag">Quality Home Builders</div>

  <div class="band band--offer">$500 Minimum or 10% Per Referral!</div>
  <div class="band band--partner">Partner with the #1 Water Damage Restoration Team</div>

  <div class="benefits">
    <h2 class="benefits__title">Why Partner with Us?</h2>
    <ul class="benefits__list">
      <li class="benefits__item"><span class="benefits__label">Guaranteed Payout:</span> Minimum $500 or 10% per job.</li>
      <li class="benefits__item"><span class="benefits__label">Free Evaluations:</span> We assess damage at no cost.</li>
      <li class="benefits__item"><span class="benefits__label">Industry Leaders:</span> Certified experts with years of experience.</li>
      <li class="benefits__item"><span class="benefits__label">Affordable Solutions:</span> Lowest out-of-pocket costs for clients.</li>
    </ul>
  </div>

  <p class="front-cta">Send Referrals, Get Paid, Repeat!</p>
</section>

<section class="flyer flyer--back" aria-label="Flyer back">
  <div class="collage">
    <div class="collage__tile collage__tile--a" role="img" aria-label="Photo of a worker repairing drywall"></div>
    <div class="collage__tile collage__tile--b" role="img" aria-label="Photo of gloved hands removing damaged wood"></div>
    <div class="collage__tile collage__tile--c" role="img" aria-label="Photo of a technician drying a water damaged room"></div>
  </div>
  <div class="cash" role="img" aria-label="Photo of stacked banknote bundles"></div>
  <div class="people" role="img" aria-label="Photo of two happy clients pointing forward"></div>

  <div class="title">
    <div class="title__small">Get Paid To</div>
    <div class="title__refer">Refer <span class="title__a">A</span></div>
    <div class="title__flood">Flood</div>
  </div>

  <div class="steps-band">How It Works</div>
  <ol class="steps">
    <li class="steps__item">1. Refer Flood, Water and Mold Damage
      <span class="steps__detail">o Call, book online, or text us directly.</span></li>
    <li class="steps__item">2. We Take Care of Everything
      <span class="steps__detail">o Free evaluations, insurance claims, and professional service.</span></li>
    <li class="steps__item">3. Get Paid Fast
      <span class="steps__detail">o $500 minimum or 10% of the invoice within 48 hours of final payment.</span></li>
  </ol>

  <div class="contact">
    <span class="contact__pill">Call Text or Book On-line</span>
    <div class="contact__phone">555-014-2290</div>
    <div class="contact__web">CoastlineRestore.com</div>
  </div>
</section>

</body>
</html>
```